BRELM - Letterhead

Willowmere Institute of Letters and Crafts (BRELM) is a non-profit organization that operates two tuition-free public schools - BRELM Elementary for grades K to 5th and BRELM College Prep for grades 6-12.

We are looking for a letterhead primarily to be used on Google Docs and Microsoft Word. Attached are two versions of our logo. One with our name spelled out and one with the acronym.

For Letterhead, we would like 3 addresses listed:

BRELM HQ
41872 Hollow Brook Lane, Suite 308
Millbrook Vale, CA 90811

BRELM Elementary (K-5)
18460 Marsh Ridge Boulevard
Millbrook Vale, CA 90811

BRELM College Prep (6-12)
27314 Del Sol Terrace
Sandpiper Bay Harbor, CA 90893

Our Phone Number is (555) 418-7062
Our Fax Number is the same (555) 418-7062

Our website is www.brelmschools.org

Target Market(s)

Education

Industry/Entity Type

Education

Font styles to use
Sans Serif

Colors
0054AA
0677BA
7BADD7
CADEEF
E8F1F8

Requirements
Must have
• Logo, Address, Phone Number, Website.
Nice to have
• Modern and clean design.
Should not have
• Prefer that there is no bleed -- the letterhead will mostly be used in PDF format however sometimes it will be printed and our printers can not do a full bleed

```html
<!DOCTYPE html>
<html lang="en">
<head>
<meta charset="utf-8">
<title>BRELM Letterhead</title>
<link href="https://fonts.googleapis.com/css2?family=Signika:wght@600&family=Josefin+Sans:wght@400;600&family=Arimo:wght@400;700&display=swap" rel="stylesheet">
<style>
  :root {
    --backdrop: #e2e2e2;
    --paper: #ebebeb;
    --brand-navy: #1b3a8f;
    --brand-blue: #0054aa;
    --ink: #111111;
    --body-grey: #858585;
    --contact-grey: #555555;
    --rule: #6a6a6a;
  }
  * { box-sizing: border-box; margin: 0; padding: 0; }
  html, body { width: 1074px; height: 1200px; overflow: hidden; }
  body { background: var(--backdrop); position: relative; }

  .letterhead {
    position: absolute; left: 74px; top: 0;
    width: 926px; height: 1200px;
    background: var(--paper);
  }

  .brand { position: absolute; left: 39px; top: 52px; display: flex; align-items: center; gap: 16px; }
  .brand-mark { width: 64px; height: 64px; background: var(--brand-navy); border-radius: 6px; }
  .brand-name {
    font-family: "Signika", sans-serif; font-weight: 600;
    font-size: 28px; line-height: 37px; color: var(--brand-navy);
  }

  .contact { position: absolute; left: 730px; top: 61px; list-style: none;
    font-family: "Josefin Sans", sans-serif; font-size: 14.5px; color: var(--contact-grey); }
  .contact li { display: flex; align-items: center; gap: 10px; height: 20.5px; }
  .contact svg { width: 14px; height: 14px; flex: none; }

  .meta-label { font-family: "Arimo", sans-serif; font-weight: 700; font-size: 17px; color: var(--ink); }
  .meta-value { font-family: "Arimo", sans-serif; font-size: 17px; color: var(--body-grey); margin-top: 4px; }
  .subject { position: absolute; left: 126px; top: 251px; }
  .date { position: absolute; left: 711px; top: 248px; }

  .letter-body { position: absolute; left: 126px; top: 405px; width: 676px;
    font-family: "Arimo", sans-serif; color: var(--body-grey); }
  .salutation { font-size: 23px; margin-bottom: 20px; }
  .letter-body p.para { font-size: 17.5px; line-height: 24px; text-align: justify; margin-bottom: 24px; hyphens: auto; }
  .letter-body p.para.full-last { text-align-last: justify; }

  .signature { position: absolute; left: 126px; top: 965px;
    font-family: "Arimo", sans-serif; font-size: 23px; line-height: 29px; color: var(--body-grey); }

  .locations { position: absolute; left: 52px; top: 1106px; display: flex;
    font-family: "Josefin Sans", sans-serif; }
  .location { font-style: normal; font-size: 14.5px; line-height: 20.5px; color: var(--contact-grey); }
  .location h3 { font-size: 15.5px; font-weight: 600; color: var(--brand-blue); line-height: 20.5px; }
  .location + .location { border-left: 1.5px solid var(--rule); }
  .location.hq { width: 269px; }
  .location.elementary { width: 297px; padding-left: 43px; }
  .location.prep { padding-left: 39px; }
</style>
</head>
<body>
<main class="letterhead">
  <header>
    <div class="brand">
      <div class="brand-mark"></div>
      <div class="brand-name">Willowmere Institute<br>of Letters and Crafts</div>
    </div>
    <ul class="contact">
      <li>
        <svg viewBox="0 0 14 14"><circle cx="7" cy="7" r="7" fill="#1b3a8f"/><path d="M4.5 4h1.6l.7 1.8-1 .7a5 5 0 0 0 1.9 1.9l.7-1 1.8.7v1.6c-3.3.4-6.1-2.4-5.7-5.7z" fill="#fff"/></svg>
        (555) 418-7062
      </li>
      <li>
        <svg viewBox="0 0 14 14"><circle cx="7" cy="7" r="7" fill="#1b3a8f"/><rect x="4" y="4.5" width="6" height="5" rx=".6" fill="#fff"/><rect x="5" y="3.2" width="4" height="2" fill="#fff"/></svg>
        (555) 418-7062
      </li>
      <li>
        <svg viewBox="0 0 14 14"><circle cx="7" cy="7" r="7" fill="#1b3a8f"/><circle cx="7" cy="7" r="3.6" fill="none" stroke="#fff" stroke-width="1"/><path d="M3.4 7h7.2M7 3.4c-1.6 2-1.6 5.2 0 7.2M7 3.4c1.6 2 1.6 5.2 0 7.2" fill="none" stroke="#fff" stroke-width=".8"/></svg>
        www.brelmschools.org
      </li>
    </ul>
  </header>

  <section class="subject">
    <div class="meta-label">SUBJECT :</div>
    <div class="meta-value">Lorem Ipsum is simply dummy</div>
  </section>
  <section class="date">
    <div class="meta-label">DATE :</div>
    <div class="meta-value">15-09-2017</div>
  </section>

  <article class="letter-body">
    <p class="salutation">Dear Person,</p>
    <p class="para full-last">Lorem Ipsum is simply dummy text of the printing and typesetting industry. Lorem Ipsum has been the industry's standard dummy text ever since the 1500s, when an unknown printer took a galley of type and scrambled it to make a type specimen book. It has survived not only five centuries, but also the leap into electronic typesetting, re&shy;maining essentially unchanged. It was popularised in the 1960s with the release of Typeframe sheets containing Lorem Ipsum passages, and more recently with desktop publishing software like Quillset Composer including versions of Lorem Ipsum.</p>
    <p class="para full-last">Lorem Ipsum is simply dummy text of the printing and typesetting industry. Lorem Ipsum has been the industry's standard dummy text ever since the 1500s, when an unknown printer took a galley of type and scrambled it to make a type specimen book. It has survived not only five centuries, but also the leap into electronic typesetting, re&shy;maining essentially unchanged. It was popularised in the 1960s with the release of</p>
    <p class="para full-last">Typeframe sheets containing Lorem Ipsum passages, and more recently with desktop publishing software like Quillset Composer including versions of Lorem Ipsum.lease of Typeframe sheets containing Lorem Ipsum passages, and more recently with desktop publishing software like Quillset Composer including versions of Lorem Ipsum. publishing software like Quillset Composer including versions of Lorem Ipsum.</p>
  </article>

  <section class="signature">
    <div>Daniel Hartwell</div>
    <div>Managing Director</div>
  </section>

  <footer class="locations">
    <address class="location hq">
      <h3>BRELM HQ</h3>
      41872 Hollow Brook Lane, Suite 308<br>Millbrook Vale, CA 90811
    </address>
    <address class="location elementary">
      <h3>BRELM Elementary (K-5)</h3>
      18460 Marsh Ridge Boulevard<br>Millbrook Vale, CA 90811
    </address>
    <address class="location prep">
      <h3>BRELM College Prep (6-12)</h3>
      27314 Del Sol Terrace<br>Sandpiper Bay Harbor, CA 90893
    </address>
  </footer>
</main>
</body>
</html>
```